依頼概要
■依頼の目的/概要
中小企業のための健康経営の電子書籍の表紙デザインをお願いします。

■本の内容
もしドライバーが、トラックを運転中に、脳梗塞や心筋梗塞を発症して、意識をなくしたら、どんなことになるでしょう。
側壁に衝突して、ドライバーがケガをする。
対向車線をはみ出し、対向車と正面衝突して、対向車のドライバーや同乗の子供たちがケガをする。
市街地で、歩道に乗り上げ、多くの歩行者がケガをする。
ケガどころか、多くの方が、命を失う可能性も少なくありません。

もしあなたが、運送会社の経営者だったら、よりリアルに想像することができて、何とも恐ろしいことになると思っていると思います。

私は、運送会社の経営者です。
数年前、私は、人生で決して忘れることのできない出来事を経験しました。

私の会社で働いていたドライバーが、心筋梗塞の症状を発症し、急死したのです。たまたま運転中ではなく、自宅から出勤するときでした。

今もその発症が、通勤途中だったらとか、トラックの運転中だったら、と考えると気が休まりません。

運送会社の経営者として、こんなことにならないように、ドライバーや一般職の社員の健康管理や健康増進を図っていく必要を強く感じています。

しかし、ドライバーあがりの運送会社の経営者は、自分の身体が丈夫なことを良く知っています。そして、自分の体を酷使してきたこともわかっているはずです。

身体を酷使してきたという事実にふたをして、自分の健康だけではなく、働くドライバーの健康のことからも、少し距離を置いていることがあるのではないでしょうか。

平成2年に物流二法が改正されてから、同業者間の競争が激しくなり、不規則な就労時間、長時間労働、不規則な食事、などドライバーの労働環境は、非常に厳しいものとなっています。

最近では、ドライバー不足が問題となっております。特に、若者の車への興味が薄れてきて、若い人材が集まらず、ドライバーの高年齢化が進んでいます。

そんな中、健康経営という言葉とともに、会社が社員の健康への関心を高め、長く、健康に働き続けられる仕組みを作ることで、社員の生産性を高めようという活動が実施され始めました。

その中でも、身体を使うドライバーを抱える運送会社こそ、社員の健康を考え、運転中の発症を防ぐことを真剣に実施していく必要があります。

運送会社の経営者が、ドライバーの健康を考え、健康増進を図れば、きっと社内が明るく活き活きした環境になっていきます。

活き活きした明るい会社になっていけば、若い人たちの注目を集め、ドライバー職に魅力を感じ、仕事として選んでくれるようになります。

人が増えれば、対応力が増し、もっと良い条件の仕事を選ぶことができます。人が増えて、良い条件の仕事をすれば、ドライバーの労働条件も改善できます。

運送会社に、若い人が集まり、労働条件が良くなれば、運送業界が活発になっていきます。運送業界が活発になれば、運送業界の地位が向上し、もっと良い人材が集まり、ますます運送業界が発展していきます。

運送会社こそ健康経営を実践してください。そして、良い運送会社、良い運送業界にしていくために、この拙著がその一助になれば幸いです。

檜原物流株式会社 代表取締役社長 柳沢 智之
健康経営アドバイザー
血管年齢測定インストラクター

■デザイン要望
中小企業が、簡単に健康管理を取り入れることができるイメージをデザインしてほしいです。病気のイメージではなく、健康という明るいイメージでお願いします。

その他何かご不明な点がございましたら、お気軽にご質問下さい。
よろしくお願いいたします。
依頼公開後の追記内容
書籍タイトル:「健康経営で地域一番の会社を作る方法」

・できるだけ視認しやすい文字でお願いします。
・あまり堅苦しくならないように、わかりやすさを重視でお願いします。

著者:中小企業の健康経営アドバイザー

色の指定はありません。(明るく、活き活き、わかりやすい)

イラストのあり、無は、お任せです。

デザイナーのみなさま、ご提案ありがとうございます。

ご提案いただいたデザインは、行政が出しているもののような堅苦しいイメージのものが多く感じます。

現行の健康経営テーマの出版物は、まさに行政関連が出しているもの、堅苦しいイメージのものばかりですので、

それらと明らかに違って見せたいと考えています。

●堅苦しい行政発信のようなイメージではなく、一般の書店のビジネス書のような印象

●健康経営 と言う文字を目立たせる

というポイントで、
少し日程を延長しますので、再提案お願いいたします。
■ 選んだ理由

緑を選定しました。
健康経営の印象が緑、健康経営を目立つようにしてある。
見た感じが他のものとは違う感じがするところが、気に入りました。

■ 提案者全員のお礼・コメント

たくさんの提案を戴きありがとうございました。
いろいろ知恵を絞ってもらい、素晴らしい提案ばかりで、選択するのが非常に難しく、レベルの高さに感激しました。
本当にありがとうございました。

```html
<!DOCTYPE html>
<html lang="ja">
<head>
<meta charset="utf-8">
<title>健康経営で地域一番の会社を作る方法</title>
<link rel="stylesheet" href="https://fonts.googleapis.com/css2?family=M+PLUS+1p:wght@500;800;900&family=M+PLUS+Rounded+1c:wght@500;800&display=swap">
<style>
  :root{
    --paper:#ffffff;
    --title-blue:#35a8dc;
    --accent-yellow:#fff03a;
    --ring-yellow:#ffe94a;
    --employee-pink:#ec5a7e;
    --company-green:#3db98a;
    --chart-green:#44b98c;
    --ink:#222222;
  }
  *{margin:0;padding:0;box-sizing:border-box}
  html,body{width:749px;height:1200px;overflow:hidden;background:var(--paper)}
  .cover{position:relative;width:749px;height:1200px;background:var(--paper);overflow:hidden;
    font-family:"M PLUS 1p",sans-serif;color:var(--title-blue)}
  .title{position:absolute;left:0;top:0;width:100%}
  .title-line{position:absolute;white-space:nowrap;font-weight:900;line-height:1;letter-spacing:2px}
  .title-line .small{font-size:62px}
  .line-1{left:92px;top:78px;font-size:112px}
  .line-2{left:92px;top:208px;font-size:112px}
  .line-3{left:92px;top:338px;font-size:112px}
  .rings{position:absolute;left:80px;top:58px}
  .infographic{position:absolute;left:40px;top:540px;width:690px;height:180px}
  .label{position:absolute;font-family:"M PLUS Rounded 1c",sans-serif;font-weight:500;letter-spacing:2px;line-height:1}
  .label-employee{left:6px;top:6px;font-size:32px;color:var(--employee-pink)}
  .label-health{left:218px;top:118px;font-size:30px;color:var(--title-blue);transform:rotate(-90deg);transform-origin:left top}
  .label-company{left:470px;top:126px;font-size:32px;color:var(--company-green)}
  .employee-icons{position:absolute;left:6px;top:52px;width:210px;height:118px;background:var(--employee-pink);opacity:.85;border-radius:6px}
  .company-icons-top{position:absolute;left:470px;top:6px;width:212px;height:104px;background:var(--company-green);opacity:.85;border-radius:6px}
  .company-icons-bottom{position:absolute;left:470px;top:166px;width:212px;height:14px;background:var(--company-green);opacity:.85;border-radius:3px}
  .growth-chart{position:absolute;left:250px;top:20px}
  .slogan-band{position:absolute;left:-40px;top:810px;width:830px;height:180px;background:var(--accent-yellow);transform:rotate(-5deg)}
  .slogan{position:absolute;left:40px;top:790px;width:680px;transform:rotate(-5deg);font-family:"M PLUS Rounded 1c",sans-serif;
    font-weight:800;color:var(--title-blue);font-size:78px;line-height:1.08;letter-spacing:2px}
  .author{position:absolute;right:40px;top:1118px;color:var(--ink);white-space:nowrap;display:flex;align-items:baseline;gap:14px}
  .author-role{font-size:22px;font-weight:800}
  .author-name{font-size:42px;font-weight:800;letter-spacing:4px}
</style>
</head>
<body>
<main class="cover">
  <svg class="rings" width="480" height="150" viewBox="0 0 480 150" aria-hidden="true">
    <g fill="none" stroke="var(--ring-yellow)" stroke-width="5">
      <circle cx="70" cy="78" r="64"/>
      <circle cx="186" cy="78" r="64"/>
      <circle cx="302" cy="78" r="64"/>
      <circle cx="418" cy="78" r="64"/>
    </g>
  </svg>
  <h1 class="title">
    <span class="title-line line-1">健康経営<span class="small">で</span></span>
    <span class="title-line line-2">地域一番<span class="small">の</span></span>
    <span class="title-line line-3">会社<span class="small">を作る方法</span></span>
  </h1>

  <section class="infographic">
    <span class="label label-employee">EMPLOYEE</span>
    <div class="employee-icons" role="img" aria-label="社員を表す人型アイコンとハートの並び"></div>
    <span class="label label-health">HEALTH</span>
    <svg class="growth-chart" width="210" height="160" viewBox="0 0 210 160" aria-hidden="true">
      <g fill="var(--chart-green)">
        <rect x="20" y="122" width="20" height="32"/>
        <rect x="56" y="104" width="20" height="50"/>
        <rect x="92" y="92" width="20" height="62"/>
        <rect x="128" y="72" width="20" height="82"/>
        <rect x="164" y="50" width="20" height="104"/>
      </g>
      <polyline points="6,4 6,156 206,156" fill="none" stroke="var(--title-blue)" stroke-width="3"/>
      <polyline points="14,112 48,84 78,96 112,62 140,72 192,18" fill="none" stroke="var(--title-blue)" stroke-width="4" stroke-linejoin="round"/>
      <polygon points="200,8 180,16 194,30" fill="var(--title-blue)"/>
    </svg>
    <div class="company-icons-top" role="img" aria-label="会社を表すビルのアイコンの並び"></div>
    <span class="label label-company">COMPANY</span>
    <div class="company-icons-bottom" role="img" aria-label="会社を表すビルのアイコンの並び"></div>
  </section>

  <div class="slogan-band" aria-hidden="true"></div>
  <p class="slogan">社員の健康管理で<br>生産性UP!!!</p>

  <p class="author"><span class="author-role">健康経営アドバイザー</span><span class="author-name">柳沢 智之</span></p>
</main>
</body>
</html>
```